Rooted Ready Rising: Quiet Roots, Open Doors, Steady Hands

I want a modern and clean looking book cover. 5.25x8

Title
Rooted Ready Rising

Subtitle
Quiet Roots, Open Doors, Steady Hands

I don’t just want a graphic, I want it to make sense. If it can just be the words and a textured looking background, I’ll be ok with that too. I just want it to look crisp, clean, modern.

I want the back to have my book blurb and bio attached with the pic that’s attached.

Target Market(s)

Self help

Requirements
Must have
• Modern, clean look, look professional, attract customers.

```html
<!DOCTYPE html>
<html lang="en">
<head>
<meta charset="utf-8">
<title>Rooted Ready Rising — Book Cover Spread</title>
<link href="https://fonts.googleapis.com/css2?family=Anton&family=Archivo:wght@800;900&family=Source+Sans+3:wght@400;700&display=swap" rel="stylesheet">
<style>
  :root {
    --page: #ffffff;
    --ink-dark: #111111;
    --ink-light: #ffffff;
    --accent-red: #ee3b30;
    --title-red: rgba(240, 50, 40, 0.82);
    --author-grey: #e6e6e6;
    --sky-top: #2f2f2f;
    --sky-mid: #8c8c8c;
    --mist: #9b9b9b;
    --forest: #1b1b1b;
  }
  * { box-sizing: border-box; margin: 0; padding: 0; }
  html, body {
    width: 1200px; height: 1000px; overflow: hidden;
    background: var(--page);
  }
  .spread {
    position: absolute; left: 0; top: 75px;
    width: 1200px; height: 850px; overflow: hidden;
  }
  .landscape {
    position: absolute; inset: 0;
    background:
      radial-gradient(ellipse 220px 140px at 548px 200px, rgba(255,255,255,0.85), rgba(255,255,255,0) 70%),
      radial-gradient(ellipse 700px 260px at 760px 320px, rgba(190,190,190,0.55), rgba(190,190,190,0) 75%),
      linear-gradient(90deg, rgba(10,10,10,0.55) 0%, rgba(10,10,10,0.15) 35%, rgba(10,10,10,0) 55%, rgba(10,10,10,0.25) 100%),
      linear-gradient(180deg, var(--sky-top) 0%, #666 12%, var(--sky-mid) 25%, var(--mist) 38%, #6e6e6e 52%, #3a3a3a 68%, var(--forest) 100%);
  }

  /* Back cover */
  .back { position: absolute; left: 0; top: 0; width: 560px; height: 850px; }
  .bio {
    position: absolute; left: 44px; top: 18px; width: 456px;
    font-family: "Source Sans 3", sans-serif; font-size: 13px; line-height: 17.4px;
    color: var(--ink-light);
  }
  .bio p { margin: 0; }
  .bio strong { font-weight: 700; }
  .bio-spacer { float: right; width: 0; height: 35px; }
  .author-photo-space { float: right; clear: right; width: 132px; height: 290px; }
  .author-photo {
    position: absolute; left: 402px; top: 95px; width: 108px; height: 262px;
    border-radius: 40px 40px 8px 8px;
    background: linear-gradient(180deg, #3a2a24 0%, #1c1c1c 35%, #e9e9e9 55%, #d8d8d8 88%, #d9342c 100%);
  }
  .tagline {
    position: absolute; left: 30px; top: 437px; width: 495px; text-align: center;
    font-family: "Source Sans 3", sans-serif; font-weight: 700; font-size: 19px; line-height: 24px;
    color: var(--accent-red);
  }
  .blurb {
    position: absolute; left: 28px; top: 498px; width: 500px; text-align: center;
    font-family: "Source Sans 3", sans-serif; font-size: 13px; line-height: 17.4px;
    color: var(--ink-light);
  }

  /* Spine */
  .spine {
    position: absolute; left: 572px; top: 186px;
    writing-mode: vertical-rl;
    font-family: Anton, "Arial Narrow", sans-serif; font-size: 33px; line-height: 42px;
    color: var(--ink-light); letter-spacing: 0.5px;
  }
  .spine-title span { display: inline-block; margin-bottom: 30px; }
  .spine-title .lead { color: var(--accent-red); }
  .spine-author {
    position: absolute; left: 580px; top: 557px; writing-mode: vertical-rl;
    font-family: Archivo, sans-serif; font-weight: 900; font-size: 19px; line-height: 26px;
    color: var(--ink-light); letter-spacing: 0.5px;
  }

  /* Front cover */
  .subtitle {
    position: absolute; left: 620px; top: 38px; width: 580px; text-align: center;
    font-family: Anton, Impact, sans-serif; font-size: 23px; letter-spacing: 0.3px;
    color: var(--ink-dark);
  }
  .title { position: absolute; inset: 0; font-weight: 400; }
  .title-line {
    position: absolute;
    font-family: Anton, Impact, sans-serif; font-size: 140px; line-height: 1;
    color: var(--title-red);
  }
  .title-line.one { left: 722px; top: 104px; }
  .title-line.two { left: 722px; top: 324px; }
  .title-line.three { right: 84px; top: 459px; }
  .author {
    position: absolute; left: 620px; top: 690px; width: 596px; text-align: center;
    font-family: Archivo, sans-serif; font-weight: 800; font-size: 36px;
    color: var(--author-grey);
  }
</style>
</head>
<body>
  <section class="spread">
    <div class="landscape" role="img" aria-label="Black and white photograph of misty forested mountains under a cloudy sky with the sun breaking through"></div>

    <div class="back">
      <div class="author-photo" role="img" aria-label="Full-length portrait of the author in a black slogan T-shirt, white jeans and red heels, hands on hips"></div>
      <div class="bio">
        <div class="bio-spacer"></div>
        <div class="author-photo-space"></div>
        <p><strong>Renata Hollis</strong> is a helper.</p>
        <p>For as long as she can remember, she’s always wanted to do the right thing, but life, circumstance, and some very tough years, set her on a path that conflicted with what was in her heart… until something clicked and she made herself and her goals a priority.</p>
        <p>A dreamer and visionary at her core, she knows all too well how much faith and courage it takes to defy expectations and build your own path forward. Her tenacity led her in a direction that would change her life for the better.</p>
        <p>After being told she wasn’t “college material” in high school, she made it her mission to never allow anyone to define who she is, and more importantly, to empower others to do the same.</p>
        <p>Today, the devout Christian, Author, Motivator, Coach, Educator, and Educational Leader, holds 3 degrees (Bachelors of Science in Psychology, Master of Education, and Educational Specialist) and is currently in the dissertation phase of a Doctorate of Education. Recently, she added Life Coach to her resume.</p>
        <p>When she’s not teaching, studying, coaching, reading, writing, listening to music, or helping others achieve their goals, she spends as much time as she can with her loving husband, three beautiful daughters, her college aged God-daughter, and countless friends.</p>
      </div>

      <p class="tagline">Everyone has big dreams and lofty goals,<br>but few give themselves permission to try.</p>

      <div class="blurb">
        <p>Rooted Ready Rising: Quiet Roots, Open Doors, Steady Hands is for anyone who has ever been stymied by negative self-talk, maltreatment, troubles at home, relationship problems, or has experienced anything significant that has made you want to abandon your dreams.</p>
        <p>Part memoir, part self-help book, part spiritual guide, this book aims to provide encouragement and a helping hand to anyone who feels like life has passed them by or think their time will never come.</p>
        <p>Inside, you’ll find deeply personal stories and anecdotes from Author Renata Hollis. Her personal experiences provide a detailed account and roadmap for how to lift yourself out of a dark spot, find your voice, dream bigger, dare to try, and change your life for the better.</p>
        <p>If you’ve ever felt like where you are now is where you’ll always be or fear that your prayers will never be answered, this book will help you move past obstacles, shatter expectations, and learn how to confidently bet on yourself because you’re worth it.</p>
      </div>
    </div>

    <div class="spine spine-title">
      <span class="lead">ROOTED</span><span>READY</span><span>RISING</span>
    </div>
    <div class="spine-author">RENATA HOLLIS</div>

    <p class="subtitle">Quiet Roots, Open Doors, Steady Hands</p>
    <h1 class="title">
      <span class="title-line one">ROOTED</span>
      <span class="title-line two">READY</span>
      <span class="title-line three">RISING</span>
    </h1>
    <p class="author">Renata Hollis</p>
  </section>
</body>
</html>
```